Business card design for Virtual Assistance company

I need a business card designed for my virtual assistance company. We are a small company who services primarily C-level executive clients. The card needs to be double sided with the following contact information on the back:
Melanie Hartwick
Owner/CEO
info@pbtadvisory.net
www.pbtadvisory.net
240.395.2817

The front side should just have the company name incorporated: "PBT Advisory" and "virtual assistance"

The card should be simplistic, but eye catching and should speak to high level executives. Our primary focus areas consist of executive assistance and government contracting.

Target Market(s)

CEOs and executives

Contact Information for Business Card

see project description. phone, email, website.

Colors

Designer to choose only greyscale colors for use in the design.

```html
<!DOCTYPE html>
<html lang="en">
<head>
<meta charset="utf-8">
<title>PBT Advisory – Business Card</title>
<link rel="stylesheet" href="https://fonts.googleapis.com/css2?family=Cinzel:wght@500;600&family=Montserrat:wght@400;500&display=swap">
<style>
  :root {
    --navy: #1b325e;
    --silver: #c9cacd;
    --grey-block: #939393;
    --card-white: #ffffff;
    --backdrop: #c6c6c6;
    --serif: "Cinzel", Georgia, serif;
    --sans: "Montserrat", Arial, sans-serif;
  }
  * { box-sizing: border-box; margin: 0; padding: 0; }
  html, body { width: 1200px; height: 800px; overflow: hidden; }
  body {
    background: var(--backdrop);
    display: flex;
    align-items: center;
    justify-content: center;
    gap: 40px;
  }
  .card {
    position: relative;
    width: 540px;
    height: 310px;
    border-radius: 18px;
    overflow: hidden;
  }
  .card--contact { background: var(--card-white); }
  .card--brand {
    background: var(--navy);
    display: flex;
    flex-direction: column;
    align-items: center;
    justify-content: center;
    gap: 10px;
  }
  .card__shapes { position: absolute; inset: 0; }
  .person {
    position: absolute;
    left: 36px;
    top: 88px;
    color: var(--navy);
  }
  .person__name {
    font-family: var(--serif);
    font-weight: 600;
    font-size: 19px;
    letter-spacing: 1px;
    text-transform: uppercase;
  }
  .person__title {
    font-family: var(--sans);
    font-size: 13px;
    margin-top: 2px;
  }
  .contact-list {
    position: absolute;
    left: 36px;
    top: 183px;
    list-style: none;
    color: #fff;
    font-family: var(--sans);
    font-size: 13px;
    line-height: 22px;
  }
  .contact-list li { display: flex; align-items: center; gap: 9px; }
  .contact-list svg { width: 13px; height: 13px; flex: none; }
  .brand-name {
    font-family: var(--serif);
    font-weight: 600;
    white-space: nowrap;
  }
  .card--contact .brand-name {
    position: absolute;
    right: 34px;
    top: 112px;
    font-size: 27px;
    color: var(--navy);
  }
  .card--brand .brand-name {
    font-size: 44px;
    color: var(--silver);
    letter-spacing: 1px;
  }
  .tagline {
    display: flex;
    align-items: center;
    gap: 10px;
    font-family: var(--sans);
    font-size: 12px;
    letter-spacing: 3px;
    text-transform: uppercase;
    color: var(--silver);
  }
  .tagline::before, .tagline::after {
    content: "";
    width: 26px;
    height: 1.5px;
    background: var(--silver);
  }
</style>
</head>
<body>
  <section class="card card--contact" aria-label="Card front with contact details">
    <svg class="card__shapes" viewBox="0 0 540 310" aria-hidden="true">
      <polygon points="372,22 508,22 508,64 440,64" fill="var(--grey-block)"/>
      <path d="M0 168 H312 Q292 214 334 262 H0 Z" fill="var(--navy)"/>
    </svg>
    <div class="person">
      <p class="person__name">Melanie Hartwick</p>
      <p class="person__title">Owner/CEO</p>
    </div>
    <ul class="contact-list">
      <li>
        <svg viewBox="0 0 24 24" fill="#fff"><path d="M6.6 10.8a15.1 15.1 0 0 0 6.6 6.6l2.2-2.2c.3-.3.7-.4 1-.2 1.1.4 2.3.6 3.6.6.6 0 1 .4 1 1V20c0 .6-.4 1-1 1A17 17 0 0 1 3 4c0-.6.4-1 1-1h3.5c.6 0 1 .4 1 1 0 1.3.2 2.5.6 3.6.1.3 0 .7-.2 1z"/></svg>
        240.395.2817
      </li>
      <li>
        <svg viewBox="0 0 24 24" fill="none" stroke="#fff" stroke-width="2.2"><rect x="2.5" y="5" width="19" height="14"/><path d="M2.5 5l9.5 8 9.5-8"/></svg>
        info@pbtadvisory.net
      </li>
      <li>
        <svg viewBox="0 0 24 24" fill="none" stroke="#fff" stroke-width="2"><circle cx="12" cy="12" r="9.5"/><path d="M2.5 12h19M12 2.5c3 3 3 16 0 19M12 2.5c-3 3-3 16 0 19"/></svg>
        www.pbtadvisory.net
      </li>
    </ul>
    <p class="brand-name">PBT Advisory</p>
  </section>

  <section class="card card--brand" aria-label="Card back with company name">
    <p class="brand-name">PBT Advisory</p>
    <p class="tagline">Virtual Assistance</p>
  </section>
</body>
</html>
```